Body therapist needs a business card

I need a card for my business which is teaching trainings in body therapy, the company is called Wexcombe Educational Group. I teach to massage therapists around Australia, South East Asia and the USA. I am attaching my logo which will guide you as to what colours I would like to have you consider. Please consult my website to find out more about what I do. www.corvantela.com.au

My name is Daniel Wexcombe. My phone number is (03) 9417 2608 or 0461753208. email is info@corvantela.com.au

```html
<!DOCTYPE html>
<html lang="en">
<head>
<meta charset="utf-8">
<title>Wexcombe Educational Group – Business Card</title>
<link rel="stylesheet" href="https://fonts.googleapis.com/css2?family=Work+Sans:wght@400;600;700&display=swap">
<style>
  :root {
    --page: #ffffff;
    --card: #ffffff;
    --brown: #9a4a00;
    --lime: #c8dc00;
    --red: #c8000a;
    --shadow: rgba(0, 0, 0, 0.07);
  }
  * { margin: 0; padding: 0; box-sizing: border-box; }
  html, body {
    width: 1200px;
    height: 1200px;
    overflow: hidden;
    background: var(--page);
    font-family: "Work Sans", Arial, sans-serif;
  }
  .card {
    position: absolute;
    left: 250px;
    width: 717px;
    height: 409px;
    background: var(--card);
    box-shadow: 0 10px 60px var(--shadow);
  }
  .card--front { top: 172px; }
  .card--back { top: 644px; }

  .brand {
    position: absolute;
    left: 40px;
    top: 60px;
    width: 320px;
    display: flex;
    flex-direction: column;
    align-items: center;
  }
  .brand__dot {
    width: 190px;
    height: 190px;
    border-radius: 50%;
    background: var(--brown);
  }
  .brand__name {
    margin-top: 22px;
    color: var(--brown);
    font-weight: 600;
    font-size: 21px;
    line-height: 1.25;
    text-align: center;
  }

  .holder-name {
    position: absolute;
    color: var(--red);
    font-weight: 700;
    font-size: 22px;
    line-height: 1.3;
    letter-spacing: 0.14em;
    text-transform: uppercase;
  }
  .card--front .holder-name { left: 423px; top: 176px; }
  .card--back .holder-name { left: 244px; top: 80px; }

  .contact {
    position: absolute;
    left: 176px;
    display: flex;
    align-items: flex-start;
    gap: 26px;
    color: var(--red);
    font-size: 23px;
    line-height: 38px;
    font-weight: 400;
  }
  .contact--phone { top: 188px; }
  .contact--email { top: 293px; }
  .contact__icon {
    width: 42px;
    height: 38px;
    flex: none;
  }
  .contact__icon path, .contact__icon rect { fill: var(--lime); }
</style>
</head>
<body>
  <section class="card card--front">
    <div class="brand">
      <div class="brand__dot"></div>
      <p class="brand__name">Wexcombe Educational Group</p>
    </div>
    <h1 class="holder-name">Daniel<br>Wexcombe</h1>
  </section>

  <section class="card card--back">
    <h2 class="holder-name">Daniel<br>Wexcombe</h2>

    <div class="contact contact--phone">
      <svg class="contact__icon" viewBox="0 0 42 38" aria-hidden="true">
        <path d="M8 3 C5 4 3 7 4 11 C7 21 15 30 26 35 C30 36 33 34 35 31 L30 25 C29 24 27 24 26 25 L23 27 C18 24 14 19 12 14 L15 11 C16 10 16 8 15 7 Z"/>
      </svg>
      <p>(03) 9417 2608<br>(04) 6175 3208</p>
    </div>

    <div class="contact contact--email">
      <svg class="contact__icon" viewBox="0 0 42 38" aria-hidden="true">
        <path d="M2 9 H40 V31 H2 Z M5 11 L21 23 L37 11 Z M4 29 H38 L27 20 L21 25 L15 20 Z" fill-rule="evenodd"/>
      </svg>
      <p>info@corvantela.com.au</p>
    </div>
  </section>
</body>
</html>
```